Fernlee Shopping Centre main sign re-design project

We would like to refresh the look of the main sign we have on the corner of a block of shops to make it more contemproary and vibrant.

A picture of the existing sign which reads Fernlee Shopping Centre can be found in attached PDF and at the following URL.

http://www.quornvale-example.co.nz/~/media/Listings/Region%20One/Town%20Centre/Central%20District/481297/Images/481297_1.ashx?bc=Gainsboro&as=1&h=550&w=980&ma=1

Fernlee Shopping Centre is also know locally as Fernlee Plaza, but the key word is Fernlee.

The existing signage has a flower/clover pattern on it which I think was just added to create a bit of interest. The building is located in a town surrounded by farm land.

I do quite like the organic feel of plant leaves or certain flowers - preferably New Zealand native plants for instance - the Kowhai flower or leaf block, pohutukawa, or kaka beak - reference images can be found with google image search

Geometric patterns could also be an option.

Once again the imagery is only to soften the sign and add some interest.
Updates

Target Market(s)

The target audience is premium shopper

Industry/Entity Type

Building

Requirements
Must have
• Must have the words: Fernlee Shopping Centre.
The big M is not essential, and I would rather the emphasis was on the word Fernlee.
Should not have
• Should not be brown. We want the sign to feel more contemporary, but not too hard. The current pale brown feels too soft in comparison with the look of the building.

```html
<!DOCTYPE html>
<html lang="en">
<head>
<meta charset="utf-8">
<title>Fernlee Shopping Centre – Main Sign</title>
<link href="https://fonts.googleapis.com/css2?family=Jost:wght@500;600&display=swap" rel="stylesheet">
<style>
  :root {
    --sign-black: #000000;
    --bloom-red: #e3140c;
    --bloom-deep: #8a0a06;
    --foliage-dark: #120806;
    --band-tint: rgba(38, 2, 0, 0.78);
    --letter-white: #ffffff;
    --letter-edge: #b0120c;
  }
  html, body {
    margin: 0;
    padding: 0;
    width: 718px;
    height: 1200px;
    overflow: hidden;
    background: var(--sign-black);
  }
  .sign {
    position: relative;
    width: 718px;
    height: 1200px;
    background: var(--sign-black);
  }
  .sign__art {
    position: absolute;
    left: 0;
    top: 0;
    width: 718px;
    height: 1200px;
    display: block;
  }
  .sign__word {
    font-family: "Jost", "Futura", sans-serif;
    fill: var(--letter-white);
    stroke: var(--letter-edge);
    paint-order: stroke fill;
    stroke-linejoin: round;
  }
  .sign__word--name { font-weight: 600; font-size: 138px; stroke-width: 5; }
  .sign__word--shopping { font-weight: 500; font-size: 96px; stroke-width: 4; }
  .sign__word--centre { font-weight: 500; font-size: 66px; stroke-width: 3.5; }
</style>
</head>
<body>
<main class="sign">
  <svg class="sign__art" viewBox="0 0 718 1200" xmlns="http://www.w3.org/2000/svg">
    <defs>
      <radialGradient id="bloomGlow" cx="0.5" cy="0.52" r="0.62">
        <stop offset="0" stop-color="var(--bloom-red)"/>
        <stop offset="0.55" stop-color="var(--bloom-deep)"/>
        <stop offset="1" stop-color="var(--foliage-dark)"/>
      </radialGradient>
    </defs>

    <rect class="sign__photo" x="24" y="108" width="666" height="1002" fill="url(#bloomGlow)"
          role="img" aria-label="Close-up photograph of red pohutukawa blossoms against dark foliage"/>

    <rect class="sign__band sign__band--name" x="24" y="270" width="666" height="210" fill="var(--band-tint)"/>
    <rect class="sign__band sign__band--type" x="24" y="782" width="666" height="208" fill="var(--band-tint)"/>

    <text class="sign__word sign__word--name" x="30" y="426" textLength="656" lengthAdjust="spacingAndGlyphs">FERNLEE</text>
    <text class="sign__word sign__word--shopping" x="354" y="874" text-anchor="middle">Shopping</text>
    <text class="sign__word sign__word--centre" x="354" y="970" text-anchor="middle">Centre</text>
  </svg>
</main>
</body>
</html>
```